Professional Business card

I need a business card to send with all my shipments. It needs to look very professional as I am branding myself, more than I am branding my company. The website is not active yet but that along with the instagram is very important as this will be moving shortly. The next required to be included is listed

Target Market(s)

All

Contact Information for Business Card

Very professional and sleek, I am trying to look like the CEO, motivational speaker and future president I plan to be

Colors
ffcf3e

Requirements
Must have
• Front

Dean Kolwick
CEO
Vendora Franchiser
Business Consultant/Start Up Guidance
Motivational Speaker
President of The United States 2040
www.deankolwick-example.com
[Instagram] @deankolwick

Back
I teach the success method used by my company you just bought from. Learn the unique model and start your own Vendora franchise today
Nice to have
• Black and Gold lettering
Should not have
• Playful vibes

```html
<!DOCTYPE html>
<html lang="en">
<head>
<meta charset="utf-8">
<title>Dean Kolwick – Business Card</title>
<link rel="stylesheet" href="https://fonts.googleapis.com/css2?family=Montserrat:wght@400;500;600&family=Raleway:wght@400;500&display=swap">
<style>
  :root {
    --backdrop: #2a2a2e;
    --card-front: #f7f7f7;
    --card-back: #1f1f1f;
    --gold: #ffcf3e;
    --ink: #2b2b2b;
    --ink-light: #ffffff;
  }
  * { margin: 0; padding: 0; box-sizing: border-box; }
  html, body {
    width: 1200px;
    height: 786px;
    overflow: hidden;
    background: var(--backdrop);
  }
  .stage {
    width: 1200px;
    height: 786px;
    display: flex;
    align-items: center;
    justify-content: center;
    gap: 40px;
  }
  .card {
    width: 520px;
    height: 297px;
    position: relative;
    box-shadow: 0 10px 30px rgba(0,0,0,0.45);
  }
  .card--front {
    background: var(--card-front);
    font-family: "Montserrat", sans-serif;
    color: var(--ink);
  }
  .front-content {
    position: absolute;
    left: 38px;
    bottom: 26px;
    width: 300px;
  }
  .name {
    font-size: 23px;
    font-weight: 500;
    letter-spacing: 1.5px;
    text-transform: uppercase;
    color: var(--gold);
    line-height: 1.1;
  }
  .role {
    font-size: 11px;
    line-height: 1.45;
    margin-top: 4px;
  }
  .rule {
    width: 270px;
    height: 1px;
    background: var(--gold);
    margin: 9px 0 10px;
  }
  .services {
    list-style: none;
    font-size: 10.5px;
    line-height: 1.5;
  }
  .contact {
    display: flex;
    align-items: center;
    gap: 5px;
    font-size: 10.5px;
    margin-top: 2px;
  }
  .contact-icon {
    width: 7px;
    height: 7px;
    background: var(--gold);
    flex: none;
  }
  .contact-icon--web { border-radius: 50%; }
  .contact-icon--social { margin-left: 5px; border-radius: 1px; }
  .card--back {
    background: var(--card-back);
    display: flex;
    align-items: center;
    justify-content: center;
  }
  .tagline {
    font-family: "Raleway", sans-serif;
    font-weight: 500;
    color: var(--ink-light);
    font-size: 13px;
    line-height: 1.4;
    text-align: center;
    width: 320px;
  }
</style>
</head>
<body>
<main class="stage">
  <section class="card card--front">
    <div class="front-content">
      <h1 class="name">Dean Kolwick</h1>
      <p class="role">CEO<br>Vendora Franchiser</p>
      <div class="rule"></div>
      <ul class="services">
        <li>Business Consultant/Start Up Guidance</li>
        <li>Motivational Speaker</li>
        <li>President of The United States 2040</li>
      </ul>
      <p class="contact">
        <span class="contact-icon contact-icon--web"></span>
        <span class="contact-web">www.deankolwick-example.com</span>
        <span class="contact-icon contact-icon--social"></span>
        <span class="contact-social">@deankolwick</span>
      </p>
    </div>
  </section>
  <section class="card card--back">
    <p class="tagline">I teach the success method used by my company you just bought from. Learn the unique model and start your own Vendora franchise today</p>
  </section>
</main>
</body>
</html>
```